Brochure to attract insurance agents to outsource their bookkeeping

I need a brochure to handout at trade shows. Company name is Corvane Policy Ledger & Records. We go by CPLR. We provide bookkeeping services. I have attached the current brochure, which is a few years old, stale and outdated (not created on PixelHerd). I have also attached our graphic identity manual which show fonts/colors as well as our logo in 3 styles

Insurance Agents needing bookkeeping services

Accounting

• See the graphic id manual

00AB8E
00BBA5
67D7C9
C6EFE9
E9F9F6

• Services noted (see current brochure), contact info, reference to Vantor Suite

```html
<!DOCTYPE html>
<html lang="en">
<head>
<meta charset="utf-8">
<title>CPLR Brochure</title>
<link href="https://fonts.googleapis.com/css2?family=Exo+2:wght@500;600;700&family=Roboto:wght@400;500;700&display=swap" rel="stylesheet">
<style>
:root{
  --teal-deep:#00AB8E;
  --teal:#00BBA5;
  --teal-soft:#67D7C9;
  --teal-pale:#C6EFE9;
  --teal-mist:#E9F9F6;
  --grey:#8a8a8a;
  --grey-dark:#4a4a4a;
  --ink:#333;
  --white:#fff;
  --stage:#000;
}
*{box-sizing:border-box;margin:0;padding:0}
html,body{width:838px;height:1200px;overflow:hidden;background:var(--stage)}
body{position:relative;font-family:"Roboto",Arial,sans-serif;color:var(--ink)}
.page{position:absolute;width:364px;height:468px;background:var(--white);overflow:hidden}
.page-team{left:43px;top:91px}
.page-cover{left:431px;top:91px}
.page-process{left:43px;top:603px}
.page-fees{left:431px;top:603px}
.abs{position:absolute}
.head{font-family:"Exo 2",Arial,sans-serif;font-weight:600;text-transform:uppercase;line-height:1.05}
.pale-fill{background:linear-gradient(180deg,var(--teal-mist),#f6fbfb 60%,#eef4f6)}

/* team page */
.team-band{left:0;top:0;width:364px;height:207px;background:var(--teal)}
.team-title{left:88px;top:0;width:187px;height:29px;background:var(--white);color:var(--teal-deep);font-size:14px;display:flex;align-items:center;justify-content:center}
.member{width:118px;text-align:center;color:var(--white)}
.member .portrait{width:55px;height:55px;border-radius:50%;margin:0 auto 4px;border:2px solid var(--white);background:linear-gradient(160deg,#9aa9ad,#5e6b70)}
.member .name{font-family:"Roboto",Arial,sans-serif;font-weight:700;font-size:7.5px;text-transform:uppercase;line-height:1.1;letter-spacing:.1px}
.member .role{font-size:7px;line-height:1.2}
.mission-title{left:0;top:222px;width:364px;text-align:center;color:var(--teal-deep);font-size:13px;text-decoration:underline}
.mission-text{left:30px;top:246px;width:304px;text-align:center;font-size:6.4px;line-height:1.55;color:var(--grey)}
.staff-bar{left:0;top:292px;width:364px;height:17px;background:var(--teal-soft);color:var(--white);font-size:6.4px;display:flex;align-items:center;justify-content:center}
.lower{left:0;top:309px;width:364px;height:159px}
.success-box{left:27px;top:326px;width:114px;height:142px;background:var(--teal);color:var(--white);font-size:12px;line-height:1.3;display:flex;align-items:center;justify-content:center;text-align:center;padding:0 8px}
.brand{display:flex;align-items:center;gap:5px;color:var(--teal-deep);font-family:"Exo 2",sans-serif;font-weight:700;text-transform:uppercase;line-height:1.05}
.brand .mark{width:12px;height:12px;background:var(--teal-deep);flex:none}
.brand-contact{left:175px;top:342px;width:160px;font-size:10px}
.contact{left:167px;top:383px;font-size:6.6px;color:var(--grey);line-height:1.55;list-style:none}
.contact li{display:flex;align-items:flex-start;gap:4px}
.contact svg{width:7px;height:7px;margin-top:2px;flex:none;fill:var(--teal-deep)}
.contact .indent{padding-left:11px}

/* cover page */
.cover-photo{left:0;top:0;width:364px;height:207px;background:linear-gradient(135deg,#dfe6ea,#f4f6f7 45%,#c9d3d8)}
.brand-box{left:0;top:207px;width:116px;height:87px;background:var(--white);padding:0 8px}
.brand-cover{height:100%;font-size:11px}
.cover-head{left:116px;top:207px;width:248px;height:87px;background:var(--teal);color:var(--white);padding:10px 14px}
.cover-head h1{font-size:16px;font-weight:600;padding-bottom:5px;border-bottom:1px solid rgba(255,255,255,.7);display:inline-block}
.cover-head p{font-size:9.5px;line-height:1.25;margin-top:6px}
.bar-services{left:0;top:294px;width:116px;height:15px;background:var(--teal);color:var(--white);font-size:7.5px;display:flex;align-items:center;justify-content:center}
.bar-web{left:116px;top:294px;width:248px;height:15px;background:var(--grey);color:var(--white);font-size:7.5px;display:flex;align-items:center;padding-left:15px}
.services{left:0;top:309px;width:364px;height:159px}
.service{width:86px;text-align:center;font-size:6.2px;color:var(--grey-dark);line-height:1.3}
.service .icon{width:34px;height:34px;border-radius:50%;border:2px solid var(--teal-pale);background:var(--white);margin:0 auto 5px;display:flex;align-items:center;justify-content:center;box-shadow:0 0 0 3px rgba(198,239,233,.5)}
.service svg{width:20px;height:20px;fill:none;stroke:var(--teal-deep);stroke-width:1.6;stroke-linecap:round;stroke-linejoin:round}

/* process page */
.process-title{left:55px;top:0;width:254px;height:36px;background:var(--teal);color:var(--white);font-size:13px;display:flex;align-items:center;justify-content:center}
.intro{left:19px;top:48px;width:330px;font-size:6.6px;line-height:1.5;color:var(--ink)}
.step{left:0;height:44px;display:flex;align-items:center;clip-path:polygon(0 0,calc(100% - 12px) 0,100% 50%,calc(100% - 12px) 100%,0 100%)}
.step .num{font-family:"Exo 2",sans-serif;font-weight:600;font-size:22px;width:46px;text-align:center;flex:none}
.step .txt{font-size:6.6px;line-height:1.4;padding-right:18px}
.step-light{background:var(--teal-mist);color:var(--ink)}
.step-light .num{color:var(--teal-deep)}
.step-mid{background:var(--teal);color:var(--white)}
.step-deep{background:var(--teal-deep);color:var(--white)}
.step-plain{background:var(--white);color:var(--ink)}
.step-plain .num{color:var(--teal-deep)}
.person-photo{left:247px;top:316px;width:107px;height:152px;background:linear-gradient(180deg,#e7ecee,#8b9396);border-radius:50px 50px 0 0}

/* fees page */
.why-panel{left:0;top:0;width:212px;height:468px;background:var(--teal)}
.why-title{left:31px;top:22px;width:181px;height:35px;background:var(--white);color:var(--grey);font-size:12px;padding:5px 10px}
.fees-title{left:212px;top:22px;width:152px;height:35px;background:var(--grey);color:var(--white);font-size:12px;padding:5px 9px}
.reason{left:12px;width:192px;color:var(--white);display:flex;gap:5px}
.reason svg{width:16px;height:16px;flex:none;fill:none;stroke:var(--white);stroke-width:2}
.reason h3{font-family:"Exo 2",sans-serif;font-weight:600;font-size:7px;text-decoration:underline;text-transform:uppercase;line-height:1.3;margin-bottom:3px}
.reason p{font-size:5.6px;line-height:1.45}
.calc-photo{left:218px;top:68px;width:146px;height:72px;background:linear-gradient(135deg,#f1f4f5,#c8d0d4 55%,#e9eef0)}
.fee-note{left:222px;top:148px;width:136px;font-size:5.8px;line-height:1.45;color:var(--ink)}
.fee-table{left:222px;top:235px;width:120px;border-collapse:collapse;font-size:6.4px}
.fee-table th{background:var(--grey);color:var(--white);font-weight:500;text-align:left;padding:3px 4px;line-height:1.15;height:30px;vertical-align:top;border-right:2px solid var(--white)}
.fee-table td{padding:1.4px 4px;height:11.2px;border-bottom:1.5px solid var(--white)}
.fee-table tbody tr:nth-child(odd) td{background:var(--teal-pale)}
.fee-table tbody tr:nth-child(even) td{background:var(--teal-mist)}
.fee-foot{left:222px;top:381px;width:130px;font-size:5.8px;line-height:1.4}
.cta-bar{left:212px;top:415px;width:152px;height:20px;background:var(--teal);color:var(--white);font-size:10.5px;display:flex;align-items:center;padding-left:10px}
.cta-phone{left:222px;top:437px;color:var(--teal);font-family:"Exo 2",sans-serif;font-weight:700;font-size:15px}
</style>
</head>
<body>

<section class="page page-team">
  <div class="abs team-band"></div>
  <h2 class="abs head team-title">CPLR Management Team</h2>
  <div class="abs member" style="left:7px;top:40px"><div class="portrait" role="img" aria-label="Portrait photo of Marlene Osterby"></div><div class="name">Marlene Osterby</div><div class="role">President</div></div>
  <div class="abs member" style="left:125px;top:40px"><div class="portrait" role="img" aria-label="Portrait photo of Evan Hallworth"></div><div class="name">Evan Hallworth</div><div class="role">Director of Accounting</div></div>
  <div class="abs member" style="left:242px;top:40px"><div class="portrait" role="img" aria-label="Portrait photo of Tessa Varlow"></div><div class="name">Tessa Varlow</div><div class="role">Manager</div></div>
  <div class="abs member" style="left:7px;top:122px"><div class="portrait" role="img" aria-label="Portrait photo of Colin Brandeis"></div><div class="name">Colin Brandeis</div><div class="role">Manager</div></div>
  <div class="abs member" style="left:125px;top:122px"><div class="portrait" role="img" aria-label="Portrait photo of Nadia Pellam"></div><div class="name">Nadia Pellam</div><div class="role">Manager</div></div>
  <div class="abs member" style="left:242px;top:122px"><div class="portrait" role="img" aria-label="Portrait photo of Owen Treadle"></div><div class="name">Owen Treadle</div><div class="role">Manager</div></div>

  <h2 class="abs head mission-title">CPLR Mission Statement:</h2>
  <p class="abs mission-text">CPLR's Mission is to provide Independent Insurance Agencies a resource to have their accounting and bookkeeping performed accurately, timely, and cost effectively.<br>CPLR offers its clients an assigned team consisting of a bookkeeper, clerk, and accountant.</p>
  <div class="abs staff-bar">For a complete list of CPLR staff, please visit www.cplrledger.com</div>

  <div class="abs lower pale-fill"></div>
  <div class="abs head success-box">Have CPLR be an integral part of your agency's success</div>
  <div class="abs brand brand-contact"><span class="mark"></span><span>Corvane Policy Ledger &amp; Records</span></div>
  <ul class="abs contact">
    <li><svg viewBox="0 0 10 10"><path d="M5 0a3.5 3.5 0 0 0-3.5 3.5C1.5 6 5 10 5 10s3.5-4 3.5-6.5A3.5 3.5 0 0 0 5 0zm0 5a1.4 1.4 0 1 1 0-2.8A1.4 1.4 0 0 1 5 5z"/></svg>47 Quarry Hill Lane</li>
    <li class="indent">Ashford Vale, CT 06000</li>
    <li><svg viewBox="0 0 10 10"><path d="M2 0l2 2.3-1 1.3c.6 1.3 1.6 2.3 2.9 2.9l1.3-1L9.5 7.5 8 9.8C3.8 9.3.7 6.2.2 2z"/></svg>555.014.2290</li>
    <li><svg viewBox="0 0 10 10"><path d="M0 2h10v6H0zM0 2l5 3.5L10 2" stroke="#fff" stroke-width=".8"/></svg>marlene@cplrledger.com</li>
    <li><svg viewBox="0 0 10 10"><circle cx="5" cy="5" r="5"/></svg>www.cplrledger.com</li>
  </ul>
</section>

<section class="page page-cover">
  <div class="abs cover-photo" role="img" aria-label="Photo of a laptop showing financial charts on a desk with a calculator and a hand holding a pen"></div>
  <div class="abs brand-box"><div class="brand brand-cover"><span class="mark"></span><span>Corvane Policy Ledger &amp; Records</span></div></div>
  <div class="abs cover-head">
    <h1 class="head">Need help with Vantor Suite accounting?</h1>
    <p>The leading remote bookkeeping firm<br>for Vantor Suite agencies nationwide</p>
  </div>
  <div class="abs bar-services">SERVICES AVAILABLE</div>
  <div class="abs bar-web">WWW.CPLRLEDGER.COM</div>
  <div class="abs services pale-fill"></div>

  <div class="abs service" style="left:43px;top:325px"><div class="icon"><svg viewBox="0 0 24 24"><rect x="5" y="4" width="14" height="16" rx="2"/><path d="M12 8v8M14 9.5h-3a1.3 1.3 0 0 0 0 2.5h2a1.3 1.3 0 0 1 0 2.5h-3"/></svg></div>Reconcile &amp; Pay<br>Agency Bill Premiums</div>
  <div class="abs service" style="left:138px;top:325px"><div class="icon"><svg viewBox="0 0 24 24"><rect x="5" y="3" width="14" height="18" rx="1"/><path d="M8 8h8M8 12h8M8 16h5"/></svg></div>Record Direct Bill<br>Commission</div>
  <div class="abs service" style="left:230px;top:325px"><div class="icon"><svg viewBox="0 0 24 24"><rect x="4" y="6" width="16" height="12" rx="2"/><circle cx="12" cy="12" r="3"/></svg></div>Pay Vendor<br>Invoices</div>

  <div class="abs service" style="left:9px;top:395px"><div class="icon"><svg viewBox="0 0 24 24"><rect x="4" y="5" width="16" height="15" rx="2"/><path d="M4 9h16M8 3v4M16 3v4M12 11v7M13.5 12.2h-2.3a1 1 0 0 0 0 2h1.6a1 1 0 0 1 0 2h-2.3"/></svg></div>Process Payroll</div>
  <div class="abs service" style="left:95px;top:395px"><div class="icon"><svg viewBox="0 0 24 24"><rect x="4" y="3" width="13" height="17" rx="1"/><path d="M7 8h7M7 12h7M7 16h4M19 13v7M20.5 14h-2a.9.9 0 0 0 0 1.8h1a.9.9 0 0 1 0 1.8h-2"/></svg></div>Record Deposits</div>
  <div class="abs service" style="left:181px;top:395px"><div class="icon"><svg viewBox="0 0 24 24"><rect x="5" y="3" width="12" height="18" rx="1"/><path d="M8 7h6M8 11h6M8 15h3M15 13h5v8h-5z"/></svg></div>Reconcile General<br>Ledger Accounts</div>
  <div class="abs service" style="left:267px;top:395px"><div class="icon"><svg viewBox="0 0 24 24"><rect x="4" y="3" width="13" height="17" rx="1"/><path d="M7 8h7M7 12h7M7 16h4M19 13v7M20.5 14h-2a.9.9 0 0 0 0 1.8h1a.9.9 0 0 1 0 1.8h-2"/></svg></div>Prepare &amp; Interpret<br>Financial Statements</div>
</section>

<section class="page page-process">
  <h2 class="abs head process-title">How outsourcing to CPLR works</h2>
  <p class="abs intro">We access your Vantor Suite online database in the same manner as Agency staff.<br>You provide the login credentials. Below is a high-level overview of the process.<br>A detail operational workflow is provided to each client Agency.</p>

  <div class="abs step step-light" style="top:97px;width:224px"><span class="num">01</span><span class="txt">Agency staff routes accounting documents<br>to CPLR through Vantor Suite.</span></div>
  <div class="abs step step-mid" style="top:144px;width:281px"><span class="num">02</span><span class="txt">Agency staff makes bank deposits of paper checks and cash, routing documentation to CPLR to record in Vantor Suite. CPLR records EFT transactions from bank records.</span></div>
  <div class="abs step step-deep" style="top:191px;width:305px"><span class="num">03</span><span class="txt">CPLR pays your agency bill premiums and vendors electronically when possible, or via Vantor Suite checks that you print. Agencies may choose the method.</span></div>
  <div class="abs step step-light" style="top:238px;width:319px"><span class="num">04</span><span class="txt">CPLR reconciles Agency staff invoicing on all agency bill transactions with insurance company/broker records at time of payment. We work with your staff on discrepancies.</span></div>
  <div class="abs step step-deep" style="top:285px;width:292px"><span class="num">05</span><span class="txt">CPLR records all direct bill commission at the time commission is received; this includes downloads, imports, and manual entry. You provide the commission statements or provide online access for CPLR to obtain.</span></div>
  <div class="abs step step-mid" style="top:332px;width:243px"><span class="num">06</span><span class="txt">CPLR reconciles all bank accounts in Vantor Suite with your bank's data at least twice per week. You provide the login credentials.</span></div>
  <div class="abs step step-plain" style="top:379px;width:250px"><span class="num">07</span><span class="txt">CPLR sends financial statements to Agency Principals each month.<br>We encourage review and discussion.</span></div>

  <div class="abs person-photo" role="img" aria-label="Photo of a smiling businesswoman in a grey blazer with arms folded"></div>
</section>

<section class="page page-fees">
  <div class="abs why-panel"></div>
  <h2 class="abs head why-title">Why outsourcing<br>to CPLR works</h2>
  <h2 class="abs head fees-title">How the CPLR fees<br>are structured</h2>

  <div class="abs reason" style="top:80px">
    <svg viewBox="0 0 16 16"><rect x="1" y="3" width="12" height="12"/><path d="M4 8l3 3 8-9"/></svg>
    <div><h3>Our staff is educated in accounting<br>&amp; trained in Vantor Suite</h3>
    <p>The CPLR staff consists of Accountants, Bookkeepers, and Clerks. All are well trained in their responsibilities for Vantor Suite accounting. Accountants have earned bachelor's degrees in accounting and have several years of Vantor Suite experience; Bookkeepers have earned associate degree credits in accounting or have significant bookkeeping experience; Clerks have a variety of experiences and education levels, many are in school for accounting, all are detail oriented numbers people. Agency clients get the benefit of a full CPLR team.</p></div>
  </div>
  <div class="abs reason" style="top:204px">
    <svg viewBox="0 0 16 16"><rect x="1" y="3" width="12" height="12"/><path d="M4 8l3 3 8-9"/></svg>
    <div><h3>Our work goes through a quality<br>control process</h3>
    <p>CPLR has a proprietary system of checks and balances to ensure client's financial statements are complete and accurate. All financial statement packages are prepared by our bookkeeping staff and reviewed by a staff accountant before presentation to the client. Agency principals are encouraged to discuss their statements with their CPLR accountant. Our goal is for our clients to understand their financial data, empowering them to make sound financial decisions.</p></div>
  </div>
  <div class="abs reason" style="top:308px">
    <svg viewBox="0 0 16 16"><rect x="1" y="3" width="12" height="12"/><path d="M4 8l3 3 8-9"/></svg>
    <div><h3>We always have a backup</h3>
    <p>When your CPLR Bookkeeper is out of the office a backup is always available. Should your CPLR Bookkeeper leave CPLR, another trained staff member will be available.</p></div>
  </div>
  <div class="abs reason" style="top:358px">
    <svg viewBox="0 0 16 16"><rect x="1" y="3" width="12" height="12"/><path d="M4 8l3 3 8-9"/></svg>
    <div><h3>We implement controls for<br>data security</h3>
    <p>All computer equipment is owned by CPLR. PCs and routers are regularly updated to stay current with technology. All are continuously monitored for operating system updates and virus/malware by an independent IT firm. Multi-factor authentication is required for access to our PCs. Documents are securely shared through Vantor Suite.</p></div>
  </div>

  <div class="abs calc-photo" role="img" aria-label="Photo of a hand pressing keys on a calculator"></div>
  <p class="abs fee-note">Fees are a flat monthly rate based on annual policy commission revenue. The table below lists sample rates for our full-service offerings at different revenue volumes for an Agency with a typical mix of business and complexity. Fees assume compliance with our standard operating workflows. Fees are updated annually and 60 days' notice is provided.</p>

  <table class="abs fee-table">
    <thead><tr><th>Annual<br>Commission<br>Revenue</th><th>Monthly<br>Service<br>Fee</th></tr></thead>
    <tbody>
      <tr><td>&lt;$300,000</td><td>$600</td></tr>
      <tr><td>$700,000</td><td>$1,500</td></tr>
      <tr><td>$1,000,000</td><td>$2,200</td></tr>
      <tr><td>$1,500,000</td><td>$2,700</td></tr>
      <tr><td>$2,000,000</td><td>$3,200</td></tr>
      <tr><td>$2,500,000</td><td>$3,800</td></tr>
      <tr><td>$3,000,000</td><td>$4,800</td></tr>
      <tr><td>$3,500,000</td><td>$5,800</td></tr>
      <tr><td>$4,000,000</td><td>$6,700</td></tr>
    </tbody>
  </table>
  <p class="abs fee-foot">We can provide services for larger agencies, typically supplementing in-house staff.</p>

  <div class="abs head cta-bar">Call/Text us today</div>
  <div class="abs cta-phone">555.014.2290</div>
</section>

</body>
</html>
```